MyRiverbendGroove Web Site Header

Potential designers can visit the site (MyRiverbendGroove.com) to see our current header. The orange color CANNOT CHANGE! Please do not submit anything different colors. The header needs to contain the following items:
-MyRiverbendGroove.com
-Catch Every Single Beat (There IS NO "?" BEHIND THIS!)
- 404.582.3967

I've supplied 13 different photos that you can choose from as a background.

Images of 920 x 150 pixels are the "exact size" that will fit my site. If it's larger, and I have to crop on uploading, I could lose text along the edges. (for what that info is worth!)

Background: Midtown Atlanta is the urban living core of Atlanta. Filled with highrise condominiums, restaurants, shopping and is also called the Heart of the Arts because Lark Playhouse and Crane Gallery are located there. It's a diverse mixture of people that live there, as well as all the office buildings that are filled daily.

The final design should give a feel of excitement, hence our tagline, Catch Every Single Beat.
Updates

Project Deadline Extended
Reason: I've gotten some INCREDIBLE designs. It's been hard to make a decision. In fact, may have to select more than one. I'm also in the middle of another project and have been swamped with it.

Target Market(s)

Target market is condo buyers. Age range from 20's to 50's. Heavy concentration of law offices and high-tech companies in the area...so think techy consumer.

Industry/Entity Type

Shopping

Font styles to use
Sans Serif

Colors
f37022

Requirements
Must have
• Phone Number 404.582.3967 or 404-582-3967

MyRiverbendGroove.com site name in header

```html
<!DOCTYPE html>
<html lang="en">
<head>
<meta charset="utf-8">
<title>MyRiverbendGroove.com</title>
<link href="https://fonts.googleapis.com/css2?family=Oswald:wght@400;500&family=Arimo:wght@400;700&display=swap" rel="stylesheet">
<style>
  :root {
    --brand-orange: #f37022;
    --brand-orange-light: #f9a04a;
    --page-bg: #b0c6e2;
    --panel-bg: #f4f4f4;
    --nav-bg: #f3f3f3;
    --nav-line: #dcdcdc;
    --link-blue: #4a90c6;
    --text: #444;
    --heading: #333;
    --divider: #e2e2e2;
  }
  * { box-sizing: border-box; margin: 0; padding: 0; }
  html, body { width: 1200px; height: 1000px; overflow: hidden; }
  body { background: var(--page-bg); font-family: "Arimo", Arial, sans-serif; position: relative; }
  .page { position: absolute; left: 96px; top: 6px; width: 1005px; height: 1000px; background: #fff; }
  .abs { position: absolute; }

  /* header */
  .brand-panel { left: 10px; top: 0; width: 244px; height: 160px; background: linear-gradient(135deg, var(--brand-orange-light), var(--brand-orange)); display: flex; align-items: center; padding-left: 20px; }
  .brand-name { font-family: "Oswald", sans-serif; font-weight: 500; font-size: 22px; color: #fff; line-height: 1.1; white-space: nowrap; }
  .header-photos { left: 254px; top: 0; width: 740px; height: 160px; display: flex; }
  .photo { height: 160px; }
  .photo-skyline { width: 331px; background: linear-gradient(#8fb4e0 0%, #c4d7ee 45%, #6f8a4e 75%, #7c8a55 100%); }
  .photo-pool { width: 240px; background: linear-gradient(#6f9560 0%, #a9c3d8 45%, #3f8ed0 70%, #d8d8d0 100%); }
  .photo-tower { width: 169px; background: linear-gradient(#2f7fd8 0%, #8ab6e6 55%, #5f8f45 100%); }
  .header-bar { left: 230px; top: 136px; width: 764px; height: 24px; background: rgba(255,255,255,.78); }
  .tagline { left: 250px; top: 135px; font-family: "Oswald", sans-serif; font-weight: 500; font-size: 19px; color: var(--brand-orange); text-transform: uppercase; }
  .header-phone { right: 28px; top: 135px; font-family: "Oswald", sans-serif; font-weight: 500; font-size: 19px; color: var(--brand-orange); }

  /* nav */
  .main-nav { left: 10px; top: 161px; width: 984px; height: 40px; background: var(--nav-bg); border-bottom: 1px solid var(--nav-line); display: flex; }
  .main-nav a { font-family: "Oswald", sans-serif; font-weight: 400; font-size: 15px; color: var(--link-blue); text-decoration: none; text-transform: uppercase; display: flex; align-items: center; justify-content: center; border-right: 1px solid var(--nav-line); white-space: nowrap; }
  .main-nav a.current { color: #222; background: #fff; }

  /* feature tiles */
  .tile-city { left: 47px; top: 244px; width: 187px; height: 134px; background: linear-gradient(135deg, #1a1a2e, #6a3aa0 50%, #2ab0c8); }
  .tile-savings { left: 259px; top: 252px; width: 163px; height: 117px; background: linear-gradient(135deg, #e9e4c8, #b8b8b8); }
  .tile-market { left: 473px; top: 243px; width: 161px; height: 137px; background: linear-gradient(135deg, #fff7c8, #c8e2f2); border: 1px solid #ccc; }
  .cta { font-family: "Oswald", sans-serif; font-weight: 500; font-size: 24px; line-height: 1.1; color: #fff; text-align: center; display: flex; align-items: center; justify-content: center; background: linear-gradient(#fcc26a, var(--brand-orange) 60%, #d85c10); border: 5px solid #fff; border-radius: 6px; box-shadow: 0 0 0 1px #ccc, 2px 3px 4px rgba(0,0,0,.35); text-shadow: 1px 1px 0 #333; }
  .cta-search { left: 50px; top: 418px; width: 174px; height: 92px; }
  .cta-worth { left: 249px; top: 416px; width: 208px; height: 95px; }
  .cta-market { left: 475px; top: 416px; width: 159px; height: 95px; }

  /* articles */
  .section-title { left: 21px; top: 530px; font-family: "Oswald", sans-serif; font-weight: 400; font-size: 17px; color: var(--heading); }
  .article { left: 21px; width: 641px; }
  .article-thumb { position: absolute; left: 0; top: 0; width: 171px; height: 171px; border: 1px solid #ddd; padding: 5px; background: #fff; }
  .article-thumb div { width: 100%; height: 100%; }
  .article-title { position: absolute; left: 193px; top: 0; width: 440px; font-family: "Oswald", sans-serif; font-weight: 400; font-size: 17px; line-height: 24px; color: var(--link-blue); }
  .article-text { position: absolute; left: 193px; width: 450px; font-size: 13px; line-height: 21.5px; color: var(--text); }
  .divider { left: 21px; width: 641px; height: 5px; background: repeating-linear-gradient(135deg, var(--divider) 0 2px, #fff 2px 4px); }

  /* sidebar */
  .sidebar { left: 695px; top: 217px; width: 299px; height: 790px; background: var(--panel-bg); }
  .side-heading { font-family: "Oswald", sans-serif; font-weight: 400; font-size: 17px; color: var(--heading); }
  .contact-line { font-family: "Oswald", sans-serif; font-weight: 400; font-size: 17px; color: #333; text-align: center; width: 283px; }
  .contact-line b { font-weight: 500; }
  .side-divider { left: 16px; width: 268px; height: 5px; background: repeating-linear-gradient(135deg, #d8d8d8 0 2px, var(--panel-bg) 2px 4px); }
  .search-form { left: 16px; top: 673px; }
  .search-form .row { display: flex; align-items: center; height: 28px; font-size: 13.5px; color: #333; }
  .search-form label { width: 94px; padding-left: 3px; }
  .search-form .field { width: 161px; height: 23px; background: #f0f0f0; border: 1px solid #ccc; }
</style>
</head>
<body>
<div class="page">
  <header>
    <div class="abs header-photos">
      <div class="photo photo-skyline" role="img" aria-label="Photo of a city skyline above a park with sports fields"></div>
      <div class="photo photo-pool" role="img" aria-label="Photo of a rooftop condo swimming pool"></div>
      <div class="photo photo-tower" role="img" aria-label="Photo of a glass residential high-rise tower"></div>
    </div>
    <div class="abs brand-panel"><span class="brand-name">MyRiverbendGroove.com</span></div>
    <div class="abs header-bar"></div>
    <div class="abs tagline">Catch Every Single Beat</div>
    <div class="abs header-phone">404.582.3967</div>
    <nav class="abs main-nav">
      <a class="current" style="width:69px">Home</a>
      <a style="width:156px">Search for Homes</a>
      <a style="width:94px">Midtown</a>
      <a style="width:131px">Midtown West</a>
      <a style="width:137px">Intown Atlanta</a>
      <a style="width:128px">About Campus</a>
      <a style="width:84px">Buyers</a>
      <a style="width:87px">Sellers</a>
      <a style="width:90px">Contact</a>
    </nav>
  </header>

  <main>
    <div class="abs tile-city" role="img" aria-label="Illustration of colorful city buildings at night"></div>
    <div class="abs tile-savings" role="img" aria-label="Illustration of home savings and budgeting"></div>
    <div class="abs tile-market" role="img" aria-label="Illustration of a rising market chart"></div>

    <a class="abs cta cta-search">Search<br>For Homes</a>
    <a class="abs cta cta-worth">What's My<br>Home Worth?</a>
    <a class="abs cta cta-market">How's The<br>Market</a>

    <h2 class="abs section-title">MyRiverbendGroove Featured Articles</h2>

    <article class="abs article" style="top:562px">
      <div class="article-thumb"><div role="img" aria-label="Photo of toy letter blocks" style="background:linear-gradient(135deg,#f7f7f7,#e9e9e9)"></div></div>
      <h3 class="article-title">Pre Approved Mortgage Loan - A Key to Your Next Midtown Atlanta Condo!</h3>
      <p class="article-text" style="top:53px">Have you been out looking for a new home or condo recently? Had some sticker shock with prices? Yes, the Atlanta real estate market is out of recovery mode, and is in FULL swing! Couple that with some of the lowest inventory we have seen in years, and you very well may find yourself in […]</p>
    </article>
    <div class="abs divider" style="top:744px"></div>

    <article class="abs article" style="top:765px">
      <div class="article-thumb"><div role="img" aria-label="Rendering of a busy transit station concourse" style="background:linear-gradient(#9fc0d8,#c9d6de 50%,#8c8c8c)"></div></div>
      <h3 class="article-title">Is Atlanta Ready (or Willing) For Transit?</h3>
      <p class="article-text" style="top:29px">An informative post, but some what of an editorial one as well! Atlanta is on the rise again! Cranes are coming out of the ground in Midtown and Buckhead as new apartment towers start to take shape. And yes, even the suburbs are on fire again as homes are being built and excess lot inventory […]</p>
    </article>
    <div class="abs divider" style="top:947px"></div>

    <article class="abs article" style="top:969px">
      <div class="article-thumb"><div role="img" aria-label="Green event banner graphic" style="background:#1f9a3c"></div></div>
      <h3 class="article-title" style="width:460px">Midtown Residents Circle |Mingle in Midtown March 20, 2013</h3>
    </article>
  </main>

  <aside class="abs sidebar">
    <div class="abs side-heading" style="left:16px;top:15px">Contact:</div>
    <div class="abs contact-line" style="left:8px;top:42px"><b>Dale Whitcomb</b>, GRI, Associate Broker</div>
    <div class="abs contact-line" style="left:8px;top:68px">Cell: 404.582.3967</div>
    <div class="abs" role="img" aria-label="Search Midtown Condos banner graphic" style="left:42px;top:97px;width:214px;height:96px;background:linear-gradient(#fff,#fde9d8)"></div>
    <div class="abs side-divider" style="top:241px"></div>
    <div class="abs side-heading" style="left:16px;top:262px">Living Near Larkstone Studios Atlanta</div>
    <div class="abs" role="img" aria-label="Promo photo of an open field with a click to learn more banner" style="left:16px;top:289px;width:283px;height:318px;background:linear-gradient(#cfe6f5 0%,#e6eef2 20%,#7e9a52 35%,#8a6a4a 70%,#7a5a3c 100%)"></div>
    <div class="abs side-divider" style="top:624px"></div>
    <div class="abs side-heading" style="left:16px;top:644px">Atlanta Real Estate Search</div>
    <div class="abs search-form">
      <div class="row"><label>Price Min</label><span class="field"></span></div>
      <div class="row"><label>Price Max</label><span class="field"></span></div>
      <div class="row"><label>Beds</label><span class="field"></span></div>
      <div class="row"><label>Baths</label><span class="field"></span></div>
    </div>
  </aside>
</div>
</body>
</html>
```